Finance Company need Staff ID card & Patio umbrella design

We need the following design:
1. Employee ID Card (Vertical ID Card)
2. Patio Umbrella
3. Uniform (light grey collar shirt)

Please note that our company theme is grey and gold (yellow). Any mixture is fine as well as long it's simple, nice and unique.

Website: www.hlr-vantor.com.kh
Updates

Project Deadline Extended
Reason: Dear all We would like to extend deadline for 5 days more.

Target Market(s)

Public

Industry/Entity Type

Bank

Requirements
Must have
• 1. ID Card, information needed:
• - Name of the company: HLR Microfinance Ltd
• - Staff name
• - Position
• - ID #
• - Expiry Date
• - Photo
• - Message at the back of ID: This card is property of HLR Mirofinance Ltd. If found, Please return to HLR Microfinance Ltd 023 417 509.
• 2- Patio Umbrella only need company name
• 3- Uniform only need company and color design.
Nice to have
• Gold (or Yellow) and/or grey (Light)

```html
<!DOCTYPE html>
<html lang="en">
<head>
<meta charset="utf-8">
<title>HLR Microfinance – Staff Identity Set</title>
<link rel="stylesheet" href="https://fonts.googleapis.com/css2?family=Arimo:ital,wght@1,400;1,700&family=Merriweather:wght@700&family=Montserrat:wght@500;700&family=Tinos&display=swap">
<style>
  :root {
    --backdrop: #cfcfcf;
    --gold: #d9b00f;
    --gold-bright: #f9c70c;
    --gold-deep: #e3a10a;
    --gold-text: #dba11a;
    --grey: #8e8d85;
    --grey-dark: #3c3c3c;
    --canopy-light: #ffffff;
    --canopy-shade: #efeff1;
    --pole: #b7bfc3;
    --ink: #1d1d1d;
    --card-white: #ffffff;
  }
  html, body {
    margin: 0;
    padding: 0;
    overflow: hidden;
    background: var(--backdrop);
  }
  .canvas {
    display: block;
    width: 1197px;
    height: 1200px;
  }
  .shirt-body { fill: var(--gold); }
  .shirt-trim { fill: var(--grey); }
  .shirt-neck { fill: #6f6e69; }
  .canopy-left { fill: var(--canopy-light); }
  .canopy-right { fill: var(--canopy-shade); }
  .canopy-edge { fill: var(--grey-dark); }
  .valance { fill: var(--gold-bright); }
  .valance-seam { stroke: #e0b000; stroke-width: 2; }
  .valance-name {
    font-family: "Tinos", serif;
    font-size: 21px;
    fill: #3a3a3a;
    text-anchor: middle;
  }
  .pole { fill: var(--pole); }
  .pole-grip { fill: var(--grey-dark); }
  .card-shadow { fill: #444; opacity: .55; }
  .card-white { fill: var(--card-white); }
  .card-slot { fill: var(--card-white); stroke: #9a7a10; stroke-width: 1.5; }
  .brand-dot { fill: var(--gold-deep); }
  .company-name {
    font-family: "Merriweather", serif;
    font-weight: 700;
    font-size: 22px;
    fill: var(--ink);
    text-anchor: middle;
  }
  .staff-id, .staff-role, .staff-valid {
    font-family: "Montserrat", sans-serif;
    font-weight: 500;
    fill: var(--ink);
    text-anchor: middle;
  }
  .staff-id { font-size: 23px; }
  .staff-role, .staff-valid { font-size: 21px; }
  .staff-name {
    font-family: "Montserrat", sans-serif;
    font-weight: 700;
    font-size: 42px;
    fill: var(--gold-text);
    text-anchor: middle;
  }
  .back-note {
    font-family: "Arimo", sans-serif;
    font-style: italic;
    font-size: 18px;
    fill: var(--ink);
    text-anchor: middle;
  }
  .back-note-strong { font-weight: 700; }
</style>
</head>
<body>
<svg class="canvas" viewBox="0 0 1450 1454" xmlns="http://www.w3.org/2000/svg">
  <defs>
    <linearGradient id="card-gold" x1="0" y1="0" x2="1" y2="1">
      <stop offset="0" stop-color="#e39e0a"/>
      <stop offset=".55" stop-color="#fbd437"/>
      <stop offset="1" stop-color="#f3bb10"/>
    </linearGradient>
    <radialGradient id="card-back-gold" cx=".5" cy=".45" r=".7">
      <stop offset="0" stop-color="#fde25a"/>
      <stop offset=".7" stop-color="#f8c81d"/>
      <stop offset="1" stop-color="#e5a20a"/>
    </radialGradient>
    <linearGradient id="portrait-tone" x1="0" y1="0" x2="0" y2="1">
      <stop offset="0" stop-color="#f2eeea"/>
      <stop offset=".6" stop-color="#b89683"/>
      <stop offset="1" stop-color="#2b2b2d"/>
    </linearGradient>
  </defs>

  <!-- Uniform polo -->
  <g class="uniform">
    <path class="shirt-body" d="M300,165 L210,205 L122,382 L218,425 L245,330 L238,655 Q395,705 553,655 L545,390 L560,418 L655,385 L565,205 L465,160 Q385,200 300,165 Z"/>
    <path class="shirt-trim" d="M122,378 L222,410 L217,428 L120,392 Z"/>
    <path class="shirt-trim" d="M556,400 L652,368 L656,388 L560,420 Z"/>
    <ellipse class="shirt-neck" cx="385" cy="150" rx="72" ry="28"/>
    <rect class="shirt-trim" x="367" y="200" width="31" height="118"/>
    <path class="shirt-trim" d="M300,165 L328,124 L362,120 L388,215 L298,205 Z"/>
    <path class="shirt-trim" d="M465,160 L440,122 L408,120 L380,215 L468,205 Z"/>
  </g>

  <!-- Patio umbrella -->
  <g class="umbrella">
    <path class="canopy-left" d="M1013,33 L722,255 L1013,255 Z"/>
    <path class="canopy-right" d="M1013,33 L1303,255 L1013,255 Z"/>
    <rect class="canopy-edge" x="722" y="255" width="581" height="9"/>
    <path class="valance" d="M722,264 H1303 V292 Q1303,302 1293,302 H732 Q722,302 722,292 Z"/>
    <line class="valance-seam" x1="1013" y1="264" x2="1013" y2="302"/>
    <text class="valance-name" x="863" y="290">H.L.R. MICRO FINANCE</text>
    <text class="valance-name" x="1162" y="290">H.L.R. MICRO FINANCE</text>
    <rect class="pole" x="1007" y="302" width="12" height="395" rx="3"/>
    <rect class="pole-grip" x="1007" y="628" width="12" height="57"/>
  </g>

  <!-- ID card, back -->
  <g class="id-card-back">
    <rect class="card-shadow" x="704" y="855" width="355" height="540" rx="6"/>
    <rect x="700" y="850" width="355" height="540" rx="6" fill="url(#card-back-gold)"/>
    <rect class="card-slot" x="843" y="872" width="70" height="16" rx="6"/>
    <text class="back-note" x="877" y="1070">This card is property of</text>
    <text class="back-note back-note-strong" x="877" y="1094">HLR Mirofinance Ltd.</text>
    <text class="back-note" x="877" y="1130">If found, Please return to</text>
    <text class="back-note back-note-strong" x="877" y="1154">HLR Microfinance Ltd</text>
    <text class="back-note back-note-strong" x="877" y="1178">023 417 509.</text>
  </g>

  <!-- ID card, front -->
  <g class="id-card-front">
    <rect class="card-shadow" x="356" y="780" width="410" height="580" rx="6"/>
    <rect x="352" y="775" width="410" height="580" rx="6" fill="url(#card-gold)"/>
    <path class="card-white" d="M352,1140 Q560,1110 762,1000 L762,1349 Q762,1355 756,1355 L358,1355 Q352,1355 352,1349 Z"/>
    <rect class="card-slot" x="522" y="800" width="70" height="16" rx="6"/>
    <circle class="brand-dot" cx="557" cy="878" r="30"/>
    <text class="company-name" x="557" y="945">HLR Microfinance Ltd.</text>
    <rect x="462" y="962" width="190" height="185" rx="4" fill="url(#portrait-tone)" role="img" aria-label="Staff member portrait photo"/>
    <text class="staff-id" x="557" y="1190">ID No. 20160811</text>
    <text class="staff-name" x="557" y="1240">John Doe</text>
    <text class="staff-role" x="557" y="1272">Manager</text>
    <text class="staff-valid" x="557" y="1318">Valid Until: 01/2017</text>
  </g>
</svg>
</body>
</html>
```